Visit card

Industry/Entity Type

Health Care

Contact Information for Business Card

O VITAL SYSTEMIQUE
Odile Ferrand - chef de Projet

Requirements
Must have
• 318 Rue des Tilleuls Verts 47150 BÉTHUNE Tel: 33 (0) 487 204 615 Mobile: 06 42 93 17 58 Web: www.cliniqorvane.example Contact: o.ferrand@o-vitalsystemique.example
Should not have
• Respect for color

```html
<!DOCTYPE html>
<html lang="fr">
<head>
<meta charset="utf-8">
<title>O Vital Systemique – Carte de visite</title>
<link rel="stylesheet" href="https://fonts.googleapis.com/css2?family=Montserrat:wght@400;500;600;700&display=swap">
<style>
  :root {
    --stage: #1c1d20;
    --card-white: #ffffff;
    --card-black: #0c0c0d;
    --brand-red: #e8202f;
    --brand-grey: #3d3d3f;
    --text-light: #ffffff;
  }
  * { box-sizing: border-box; margin: 0; padding: 0; }
  html, body {
    width: 1200px; height: 900px; overflow: hidden;
    background: var(--stage);
    font-family: "Montserrat", sans-serif;
  }
  .sheet {
    width: 1200px; height: 900px;
    display: flex; align-items: center; justify-content: center; gap: 40px;
  }
  .card {
    position: relative;
    width: 540px; height: 310px;
    overflow: hidden;
    box-shadow: 0 18px 40px rgba(0,0,0,.55);
  }
  .card-art { position: absolute; inset: 0; }

  /* Brand lockup */
  .brand { position: absolute; display: flex; align-items: center; gap: 16px; }
  .brand-dot { width: 62px; height: 62px; border-radius: 50%; background: var(--brand-red); flex: none; }
  .brand-name {
    font-weight: 700; font-size: 26px; line-height: 1.05; letter-spacing: 2px;
  }

  /* Front */
  .card-front { background: var(--card-white); }
  .card-front .brand { left: 150px; top: 42px; }
  .card-front .brand-name { color: var(--brand-grey); }
  .contact-list {
    position: absolute; left: 24px; top: 160px;
    list-style: none; color: var(--text-light);
    font-size: 11.5px; line-height: 19px; font-weight: 500;
    white-space: nowrap;
  }
  .contact-list li { display: flex; align-items: flex-start; gap: 8px; }
  .contact-list svg { width: 10px; height: 10px; margin-top: 4px; flex: none; }
  .contact-list .indent { padding-left: 18px; }
  .holder {
    position: absolute; right: 34px; bottom: 48px;
    color: var(--text-light); text-align: left;
  }
  .holder-name { font-size: 21px; font-weight: 600; letter-spacing: .3px; }
  .holder-role { font-size: 13px; font-weight: 400; margin-top: 2px; }

  /* Back */
  .card-back { background: var(--card-black); }
  .card-back .brand { left: 120px; top: 92px; }
  .card-back .brand-name { color: var(--text-light); font-size: 30px; }
  .back-web {
    position: absolute; left: 26px; bottom: 20px;
    color: var(--text-light); font-size: 13px; font-weight: 500; letter-spacing: .3px;
  }
</style>
</head>
<body>
<main class="sheet">

  <section class="card card-front" aria-label="Recto de la carte">
    <svg class="card-art" viewBox="0 0 540 310" preserveAspectRatio="none" aria-hidden="true">
      <polygon points="0,145 540,145 540,310 0,310" fill="var(--card-black)"/>
      <polygon points="335,145 540,145 540,310 305,310" fill="var(--brand-red)"/>
    </svg>

    <div class="brand">
      <span class="brand-dot"></span>
      <span class="brand-name">O VITAL<br>SYSTEMIQUE</span>
    </div>

    <ul class="contact-list">
      <li>
        <svg viewBox="0 0 10 10"><path d="M5 0a3.5 3.5 0 0 0-3.5 3.5C1.5 6 5 10 5 10s3.5-4 3.5-6.5A3.5 3.5 0 0 0 5 0zm0 5a1.5 1.5 0 1 1 0-3 1.5 1.5 0 0 1 0 3z" fill="var(--brand-red)"/></svg>
        <span>318 Rue des Tilleuls Verts</span>
      </li>
      <li class="indent">47150 VALMORIN</li>
      <li>
        <svg viewBox="0 0 10 10"><path d="M2 0l2 2.5-1 1.2a6 6 0 0 0 3.3 3.3l1.2-1L10 8l-1.5 2C4 10 0 6 0 1.5z" fill="var(--brand-red)"/></svg>
        <span>Tél : +33 (0) 487 204 615</span>
      </li>
      <li>
        <svg viewBox="0 0 10 10"><rect x="2.5" y=".5" width="5" height="9" rx="1" fill="none" stroke="var(--brand-red)"/></svg>
        <span>Mobil : 06 42 93 17 58</span>
      </li>
      <li>
        <svg viewBox="0 0 10 10"><circle cx="5" cy="5" r="4.4" fill="none" stroke="var(--brand-red)"/><path d="M.6 5h8.8M5 .6c-2.4 2.6-2.4 6.2 0 8.8M5 .6c2.4 2.6 2.4 6.2 0 8.8" fill="none" stroke="var(--brand-red)" stroke-width=".8"/></svg>
        <span>www.cliniqorvane.example</span>
      </li>
      <li>
        <svg viewBox="0 0 10 10"><rect x=".5" y="1.5" width="9" height="7" fill="none" stroke="var(--brand-red)"/><path d="M.5 1.5L5 5.5l4.5-4" fill="none" stroke="var(--brand-red)"/></svg>
        <span>o.ferrand@o-vitalsystemique.example</span>
      </li>
    </ul>

    <div class="holder">
      <p class="holder-name">Odile Ferrand</p>
      <p class="holder-role">Chef de Projet</p>
    </div>
  </section>

  <section class="card card-back" aria-label="Verso de la carte">
    <svg class="card-art" viewBox="0 0 540 310" preserveAspectRatio="none" aria-hidden="true">
      <polygon points="0,262 270,262 250,310 0,310" fill="var(--brand-red)"/>
    </svg>

    <div class="brand">
      <span class="brand-dot"></span>
      <span class="brand-name">O VITAL<br>SYSTEMIQUE</span>
    </div>

    <p class="back-web">www.cliniqorvane.example</p>
  </section>

</main>
</body>
</html>
```